Student Card

we are college and require a student card which we issue on enlroment to students, just like a univeristy.

Baisic information need to be placed is:
Student photo
student ID
date of birth
exp date

our college contact details on the rear
its a tool for branding so its important the theme is in line with our colours and logo, please view our website www.harlowmereinstitute.net.au

Industry/Entity Type

College

```html
<!DOCTYPE html>
<html lang="en">
<head>
<meta charset="utf-8">
<title>Harlowmere Institute – Student Card</title>
<link rel="stylesheet" href="https://fonts.googleapis.com/css2?family=Tinos:wght@400;700&display=swap">
<style>
  :root {
    --edge-blue: #4a6fb8;
    --edge-green: #5fb554;
    --edge-orange: #eea13c;
    --card-green: #9dcf6b;
    --card-green-deep: #8cc257;
    --card-orange: #eea13c;
    --photo-slot: #cdd4ea;
    --ink-dark: #2a2416;
    --ink-navy: #233a8c;
    --ink-red: #c9252b;
    --mark-navy: #2f4a9c;
    --mark-teal: #3d7f74;
    --paper: #ffffff;
  }
  * { box-sizing: border-box; margin: 0; padding: 0; }
  html, body { width: 1200px; height: 730px; overflow: hidden; background: var(--paper); }
  body { position: relative; font-family: "Tinos", "Times New Roman", serif; }

  .card { position: absolute; overflow: hidden; }
  .card-edge {
    position: absolute; inset: 5px;
    border: 6px solid transparent; border-radius: 4px;
    background: linear-gradient(90deg, var(--edge-blue), var(--edge-green), var(--edge-orange)) border-box;
    -webkit-mask: linear-gradient(#000 0 0) padding-box, linear-gradient(#000 0 0);
    -webkit-mask-composite: xor;
    mask: linear-gradient(#000 0 0) padding-box exclude, linear-gradient(#000 0 0);
    opacity: .55;
  }

  /* Front */
  .card-front {
    left: 0; top: 0; width: 601px; height: 348px;
    background: linear-gradient(180deg, var(--card-green) 0%, var(--card-green) 50%, var(--card-orange) 52%, var(--card-orange) 100%);
  }
  .front-scene {
    position: absolute; left: 190px; top: 0; width: 411px; height: 348px;
    background: linear-gradient(160deg, rgba(200,230,170,.55) 0%, rgba(170,210,140,.35) 45%, rgba(240,180,90,.5) 60%, rgba(230,150,60,.35) 100%);
  }
  .student-photo {
    position: absolute; left: 31px; top: 25px; width: 201px; height: 171px;
    background: linear-gradient(180deg, #d8deef, var(--photo-slot));
  }
  .front-brand {
    position: absolute; left: 372px; top: 62px; width: 230px; text-align: center;
  }
  .brand-dot {
    display: block; margin: 0 auto 12px; width: 70px; height: 70px; border-radius: 50%;
    background: var(--mark-teal); opacity: .85;
  }
  .brand-name { font-weight: 700; color: var(--mark-teal); font-size: 15px; white-space: nowrap; }
  .student-details { position: absolute; left: 29px; top: 202px; color: var(--ink-dark); }
  .student-name { font-size: 25px; line-height: 32px; }
  .student-field { font-size: 18px; line-height: 31px; letter-spacing: -.2px; }

  /* Back */
  .card-back { left: 615px; top: 3px; width: 582px; height: 345px; background: var(--paper); }
  .back-brand { position: absolute; left: 0; right: 0; top: 66px; text-align: center; }
  .back-brand .brand-dot { width: 130px; height: 130px; background: var(--mark-navy); margin-bottom: 30px; opacity: 1; }
  .back-brand .brand-name { color: var(--ink-dark); font-size: 26px; line-height: 30px; }
  .contact-phone { color: var(--ink-red); font-size: 32px; line-height: 34px; white-space: nowrap; }
  .contact-email { color: var(--ink-navy); font-size: 27px; line-height: 30px; white-space: nowrap; }

  /* Alternate back */
  .card-alt { left: 601px; top: 386px; width: 599px; height: 344px; background: var(--card-green-deep); }
  .alt-panel {
    position: absolute; left: 132px; top: 24px; width: 340px; height: 292px;
    background: linear-gradient(180deg, rgba(215,235,195,.75), rgba(190,222,160,.7));
  }
  .alt-brand { position: absolute; left: 0; right: 0; top: 56px; text-align: center; }
  .alt-brand .brand-dot { width: 110px; height: 110px; background: var(--mark-teal); opacity: .45; margin-bottom: 44px; }
  .alt-brand .brand-name { color: #4e5a45; font-size: 26px; line-height: 30px; opacity: .8; }
</style>
</head>
<body>

<section class="card card-front" aria-label="Student card front">
  <div class="front-scene" role="img" aria-label="Faded city skyline and group of cheerful students"></div>
  <div class="student-photo" role="img" aria-label="Student photo placeholder"></div>
  <div class="front-brand">
    <span class="brand-dot"></span>
    <p class="brand-name">HARLOWMERE INSTITUTE</p>
  </div>
  <div class="student-details">
    <p class="student-name">Name: Alex Carter</p>
    <p class="student-field">Student ID: 0101010101010</p>
    <p class="student-field">DOB: 01/01/2013</p>
    <p class="student-field">Exp: 12/02/2018</p>
  </div>
  <div class="card-edge" role="img" aria-label="Multicoloured decorative border"></div>
</section>

<section class="card card-back" aria-label="Student card back">
  <div class="back-brand">
    <span class="brand-dot"></span>
    <p class="brand-name">HARLOWMERE INSTITUTE</p>
    <p class="contact-phone">+617.5550.0142</p>
    <p class="contact-email">info@harlowmereinstitute.net.au</p>
  </div>
  <div class="card-edge" role="img" aria-label="Multicoloured decorative border"></div>
</section>

<section class="card card-alt" aria-label="Student card back, coloured version">
  <div class="alt-panel" role="img" aria-label="Faded city skyline behind the contact details"></div>
  <div class="alt-brand">
    <span class="brand-dot"></span>
    <p class="brand-name">HARLOWMERE INSTITUTE</p>
    <p class="contact-phone">+617.5550.0142</p>
    <p class="contact-email">info@harlowmereinstitute.net.au</p>
  </div>
  <div class="card-edge" role="img" aria-label="Multicoloured decorative border"></div>
</section>

</body>
</html>
```